ACCOUNTING FIRM CHRISTMAS MESSAGE AND OFFICE CLOSURE NOTIFICATION

WE WISH TO EMAIL A CHRISTMAS CARD IN EMAIL - WISHING OUR CLIENTS THE MERRY CHRISTMAS AND A SAFE, HEALTHY AND PROSPOROUS 2015. WE ALSO WOULD LIKE TO ADVISE OUR OFFICE CLOSES AT 4PM 23/12/2014 AND RE-OPENS AT 9AM ON 12TH JANUARY 2015.

Industry/Entity Type

Accounting

```html
<!DOCTYPE html>
<html lang="en">
<head>
<meta charset="utf-8">
<title>Clearline Accounting – Season's Greetings</title>
<link href="https://fonts.googleapis.com/css2?family=Great+Vibes&family=Oswald:wght@400;500&family=Special+Elite&display=swap" rel="stylesheet">
<style>
  :root {
    --red-core: #e01a1f;
    --red-mid: #b80d12;
    --red-deep: #6e0306;
    --gold: #f2cd3c;
    --gold-deep: #b8860b;
    --white: #ffffff;
    --shadow: rgba(40, 0, 0, 0.85);
    --notice-blue: #52c6f2;
    --notice-ink: #0d2f6b;
    --brand-ink: #c8261d;
  }
  html, body {
    margin: 0;
    padding: 0;
    width: 1200px;
    height: 899px;
    overflow: hidden;
    background: var(--red-deep);
  }
  .card {
    position: relative;
    width: 1200px;
    height: 899px;
    overflow: hidden;
    background:
      radial-gradient(ellipse 70% 65% at 58% 42%, var(--red-core) 0%, var(--red-mid) 55%, var(--red-deep) 100%);
  }
  .ornament-garland {
    position: absolute;
    left: 0;
    top: 0;
    width: 420px;
    height: 899px;
    background:
      radial-gradient(circle 150px at 125px 640px, rgba(240, 70, 55, 0.95), rgba(190, 25, 20, 0.6) 60%, rgba(150, 10, 10, 0) 100%),
      radial-gradient(circle 60px at 60px 590px, rgba(242, 205, 60, 0.45), rgba(242, 205, 60, 0) 100%),
      radial-gradient(ellipse 70px 300px at 110px 220px, rgba(242, 205, 60, 0.55), rgba(242, 205, 60, 0) 100%),
      radial-gradient(ellipse 60px 260px at 230px 280px, rgba(242, 205, 60, 0.45), rgba(242, 205, 60, 0) 100%),
      radial-gradient(ellipse 50px 180px at 300px 150px, rgba(242, 205, 60, 0.35), rgba(242, 205, 60, 0) 100%),
      radial-gradient(circle 40px at 300px 460px, rgba(242, 205, 60, 0.4), rgba(242, 205, 60, 0) 100%),
      linear-gradient(90deg, rgba(120, 5, 5, 0.35), rgba(120, 5, 5, 0));
  }
  .sparkle-field {
    position: absolute;
    right: 0;
    top: 0;
    width: 320px;
    height: 280px;
    background:
      radial-gradient(circle 90px at 230px 60px, rgba(255, 255, 255, 0.28), rgba(255, 255, 255, 0) 100%),
      radial-gradient(ellipse at 80% 20%, rgba(255, 255, 255, 0.14), rgba(255, 255, 255, 0) 70%);
  }
  .headline {
    position: absolute;
    left: 430px;
    top: 25px;
    width: 520px;
    margin: 0;
    font-family: 'Great Vibes', cursive;
    font-weight: 400;
    color: var(--gold);
    text-shadow: 3px 3px 0 var(--gold-deep), 5px 6px 8px var(--shadow);
    line-height: 1;
  }
  .headline .merry {
    display: block;
    font-size: 130px;
    padding-left: 80px;
  }
  .headline .christmas {
    display: block;
    font-size: 130px;
    margin-top: -30px;
  }
  .greeting {
    position: absolute;
    left: 210px;
    top: 310px;
    width: 760px;
    margin: 0;
    font-family: 'Oswald', sans-serif;
    font-weight: 400;
    font-size: 46px;
    line-height: 92px;
    color: var(--white);
    text-align: center;
    white-space: nowrap;
    text-shadow: 4px 4px 5px var(--shadow);
  }
  .greeting span { display: block; }
  .greeting .year { margin-top: -14px; }
  .notice {
    position: absolute;
    left: 660px;
    top: 655px;
    width: 600px;
    height: 170px;
    background: var(--notice-blue);
    transform: rotate(-24deg);
    transform-origin: center;
    box-shadow: 0 4px 10px rgba(0, 0, 0, 0.35);
    display: flex;
    align-items: center;
    justify-content: center;
  }
  .notice p {
    margin: 0;
    font-family: 'Special Elite', monospace;
    font-size: 25px;
    line-height: 38px;
    color: var(--notice-ink);
    text-align: center;
    white-space: nowrap;
  }
  .brand {
    position: absolute;
    left: 13px;
    top: 766px;
    width: 436px;
    height: 108px;
    background: var(--white);
    display: flex;
    align-items: center;
    justify-content: center;
    gap: 18px;
  }
  .brand-mark {
    width: 32px;
    height: 32px;
    background: var(--brand-ink);
    flex: none;
  }
  .brand-name {
    font-family: 'Oswald', sans-serif;
    font-weight: 500;
    color: var(--brand-ink);
    line-height: 1;
  }
  .brand-name .primary { display: block; font-size: 52px; letter-spacing: 2px; }
  .brand-name .secondary { display: block; font-size: 20px; letter-spacing: 1px; margin-top: 4px; }
</style>
</head>
<body>
  <main class="card">
    <div class="ornament-garland" role="img" aria-label="Gold ribbons with hanging red and gold Christmas baubles and snowflakes"></div>
    <div class="sparkle-field" role="img" aria-label="Soft white sparkles and snowflakes"></div>

    <h1 class="headline">
      <span class="merry">Merry</span>
      <span class="christmas">Christmas</span>
    </h1>

    <p class="greeting">
      <span>WISHING YOU THE MERRY CHRISTMAS</span>
      <span>AND</span>
      <span>A SAFE, HEALTHY AND PROSPEROUS</span>
      <span class="year">2015</span>
    </p>

    <div class="notice">
      <p>OFFICE CLOSES AT 4PM 23/12/2014<br>AND RE-OPENS<br>AT 9AM ON 12TH JANUARY 2015</p>
    </div>

    <div class="brand">
      <span class="brand-mark"></span>
      <span class="brand-name">
        <span class="primary">CLEARLINE</span>
        <span class="secondary">ACCOUNTING PTY LTD</span>
      </span>
    </div>
  </main>
</body>
</html>
```